Redesigning Web Pages

I need to redesign a section on my website:
http://kefor.mb-gemwork.com/en/copperleafden
The complete (Copperleaf Den) section needs to be redesigned.
The works involves designing only. I have my own development team. You would need to provide me with the designing (psd) files at the end of the project.
Please go through the whole section so that you can see the pages that needs to be redesigned (Note: you can create a demo account to see the inner pages, its ok as this link is on the development server). Again, to be clear, I need only to redesign this section (including its sub pages, like registration, user profile page, etc), not the whole website. Of course, the main page to be designed would be the section "main page" the other inner pages are to match the design of the main section page.
All features, functions, and facilities provided on the section are to remain the same.
The design needs to match the current website format. Keep in mind the look and feel information I have provided for this section. Note: Please view the highlighted area in the attached file. This is the area that needs to be redesigned.
The design would be selected based on the creativity of the designer and understanding of what needs to be done.

```html
<!DOCTYPE html>
<html lang="en">
<head>
<meta charset="utf-8">
<title>Change Password – Kefor</title>
<link href="https://fonts.googleapis.com/css2?family=Arimo:wght@400;700&display=swap" rel="stylesheet">
<style>
:root{
  --bg-top:#b6a169;
  --bg-bottom:#ddd4aa;
  --sky-bottom:#3d7fb8;
  --tan:#c1a776;
  --brown:#3a2410;
  --green:#6f7a36;
  --green-light:#8f9a4f;
  --blue-title:#2a5f9a;
  --blue-frame:#3f7fb5;
  --text:#333;
  --muted:#666;
  --field-border:#9a9a9a;
  --footer-dark:#2b2621;
  --white:#fff;
}
*{box-sizing:border-box;margin:0;padding:0}
html,body{width:1200px;height:1177px;overflow:hidden}
body{
  position:relative;
  font-family:"Arimo",Arial,sans-serif;
  color:var(--text);
  background:linear-gradient(var(--bg-top) 0,#c9b783 780px,var(--bg-bottom) 790px,var(--bg-bottom) 100%);
}
.page{position:absolute;left:157px;top:15px;width:893px;height:1162px;background:var(--tan)}
.abs{position:absolute}
.sky{left:0;top:0;width:893px;height:440px;background:linear-gradient(#8fbfe2,var(--sky-bottom) 70%,#5c8fb6)}
.header-bar{left:13px;top:38px;width:370px;height:44px;background:var(--brown);display:flex;align-items:center;padding-left:25px;gap:12px}
.header-bar .auth{color:#f2e8d0;font-size:12px;font-weight:700;letter-spacing:.2px;white-space:nowrap}
.search{width:208px;height:26px;background:var(--white);border-radius:13px;display:flex;align-items:center;justify-content:space-between;padding-left:6px;font-size:12px;color:#222}
.search .go{width:24px;height:24px;border-radius:50%;background:#d9b26a;display:flex;align-items:center;justify-content:center}
.lang{left:477px;top:0;color:var(--white);font-size:12px;font-weight:700}
.brand{left:660px;top:40px;display:flex;align-items:center;gap:10px}
.brand .dot{width:26px;height:26px;background:#e8b54a;border-radius:50%}
.brand .name{font-size:40px;font-weight:700;color:#1f5a99;letter-spacing:1px}
.main-nav{left:13px;top:113px;width:867px;height:34px;border-radius:17px;background:linear-gradient(var(--green-light),var(--green));display:flex;align-items:center;justify-content:space-around;padding:0 18px;white-space:nowrap}
.main-nav a,.sub-nav a{color:var(--white);text-decoration:none;font-size:13px}
.main-nav .sep,.sub-nav .sep{width:1px;height:18px;background:rgba(255,255,255,.5)}
.sub-nav{left:490px;top:154px;display:flex;gap:14px;align-items:center;z-index:2;white-space:nowrap}
.sub-nav a{font-size:11px}
.sub-nav .sep{height:11px}
.frame{left:13px;top:148px;width:866px;height:673px;background:var(--blue-frame);padding:23px 9px 10px;border-radius:4px}
.panel{width:100%;height:100%;background:var(--white);position:relative}
.profile-head{left:18px;top:14px;width:218px;height:38px;background:linear-gradient(#4a86c0,#2a5f9a);color:var(--white);font-size:17px;padding:9px 10px}
.stat{left:22px;font-size:12px;color:var(--text)}
.stat b{font-weight:700}
.avatar{left:18px;top:144px;width:218px;height:250px;background:linear-gradient(#efece6,#cfc4b4 60%,#5a4638);border:1px solid #ccc}
.user-name{left:18px;top:405px;font-size:19px;color:var(--blue-title)}
.menu-btn{left:18px;width:218px;height:21px;border:1px solid #ccc;background:linear-gradient(#fff,#ebebeb);font-size:11px;text-align:center;line-height:19px;color:#333}
.form-title{left:255px;top:27px;font-size:19px;color:var(--blue-title);font-weight:400}
.required{left:685px;top:40px;font-size:11px;color:var(--muted)}
.row-label{left:255px;font-size:12px;color:var(--text)}
.colon{left:420px;font-size:12px}
.field{left:434px;width:282px;height:23px;border:1px solid var(--field-border);font-size:12px;padding:4px 10px}
.save{left:634px;top:169px;width:82px;height:22px;background:linear-gradient(#77813e,#4f5a22);color:var(--white);font-size:9px;text-align:center;line-height:22px;border-radius:2px}
.col-title{top:868px;font-size:18px;font-weight:700;color:var(--white);text-align:center}
.col-box{top:902px;height:164px;background:rgba(150,125,80,.45)}
.ornament{left:0;top:821px;width:893px;height:270px;background:linear-gradient(rgba(255,255,255,0),rgba(90,65,30,.12))}
.country-list{left:16px;top:900px;width:211px;text-align:center;color:var(--white);font-size:11px;font-weight:700;line-height:26px}
.city{left:386px;top:906px;color:var(--white);font-size:11px;font-weight:700}
.login-label{right:20px;font-size:15px;font-weight:700;color:var(--white)}
.login-label span{color:#d02020}
.login-input{left:681px;width:193px;height:25px;background:var(--white);border:1px solid #999}
.login-link{right:20px;font-size:14px;color:var(--white);text-align:right;line-height:15px}
.login-btn{left:738px;top:1048px;width:61px;height:23px;background:linear-gradient(#fff,#ddd);border:1px solid #999;font-size:10px;font-weight:700;text-align:center;line-height:21px;color:#333}
.footer-line{left:0;top:1085px;width:893px;height:7px;background:#efe4c4}
.footer{left:0;top:1092px;width:893px;height:70px;background:var(--footer-dark);color:#d8cfbb;text-align:center}
.footer nav{padding-top:26px;font-size:10px;font-weight:700;letter-spacing:.3px}
.footer nav span{margin:0 6px;color:#999}
.footer .copy{font-size:10px;margin-top:5px}
</style>
</head>
<body>
<div class="page">
  <div class="abs sky" role="img" aria-label="Blue sky with soft clouds over a tiled grid"></div>
  <div class="abs lang">English | Arabic</div>
  <div class="abs header-bar">
    <span class="auth">REGISTER | SIGN IN</span>
    <div class="search">SEARCH
      <span class="go"><svg width="10" height="12" viewBox="0 0 10 12"><path d="M1 1l8 5-8 5z" fill="#fff"/></svg></span>
    </div>
  </div>
  <div class="abs brand"><span class="dot"></span><span class="name">KEFOR</span></div>

  <nav class="abs main-nav">
    <a>TRAVEL ARTICLES</a><i class="sep"></i><a>TRAVEL PHOTOS</a><i class="sep"></i><a>TOURS</a><i class="sep"></i><a>MAPS</a><i class="sep"></i><a>WEATHER</a><i class="sep"></i><a>HOTELS</a><i class="sep"></i><a>THINGS TO DO</a><i class="sep"></i><a>DESTINATIONS</a><i class="sep"></i><a>HOME</a>
  </nav>

  <div class="abs frame">
    <div class="panel">
      <div class="abs profile-head">User Profile</div>
      <div class="abs stat" style="top:74px;display:flex;align-items:center;gap:4px">
        <svg width="14" height="14" viewBox="0 0 14 14"><path d="M1 6h3v7H1zM5 6l3-5c1 0 2 1 1.5 2.5L9 6h3.5c.8 0 1.3.8 1 1.5L12 12.5c-.2.4-.6.5-1 .5H5z" fill="#2a5f9a"/></svg>
        Useful / Interesting&nbsp;&nbsp;(<b>0</b>)
      </div>
      <div class="abs stat" style="top:96px;left:40px">Points Earned (<b>1.5</b>)</div>
      <svg class="abs" style="left:40px;top:113px" width="82" height="14" viewBox="0 0 82 14">
        <defs>
          <path id="st" d="M7 1l1.8 3.8 4.2.5-3.1 2.9.8 4.2L7 10.3 3.3 12.4l.8-4.2L1 5.3l4.2-.5z"/>
          <clipPath id="half"><rect x="0" y="0" width="7" height="14"/></clipPath>
        </defs>
        <use href="#st" fill="#e8a920"/>
        <g transform="translate(16 0)">
          <use href="#st" fill="none" stroke="#bbb" stroke-width=".8"/>
          <use href="#st" fill="#e8a920" clip-path="url(#half)"/>
        </g>
        <use href="#st" x="32" fill="none" stroke="#bbb" stroke-width=".8"/>
        <use href="#st" x="48" fill="none" stroke="#bbb" stroke-width=".8"/>
        <use href="#st" x="64" fill="none" stroke="#bbb" stroke-width=".8"/>
      </svg>
      <div class="abs avatar" role="img" aria-label="Profile photo of the member"></div>
      <div class="abs user-name">Karim Nasser</div>
      <div class="abs menu-btn" style="top:440px">Edit profile</div>
      <div class="abs menu-btn" style="top:465px">Upload Profile Image</div>
      <div class="abs menu-btn" style="top:490px">Change Password</div>
      <div class="abs menu-btn" style="top:515px">Write a Travel Article</div>
      <div class="abs menu-btn" style="top:540px">Upload a Travel Photo</div>
      <div class="abs menu-btn" style="top:565px">Submit a Review</div>

      <h1 class="abs form-title">Change Password</h1>
      <div class="abs required">All fields are required</div>
      <div class="abs row-label" style="top:75px">Old password</div>
      <div class="abs colon" style="top:75px">:</div>
      <div class="abs field" style="top:69px">Karim</div>
      <div class="abs row-label" style="top:107px">New password</div>
      <div class="abs colon" style="top:107px">:</div>
      <div class="abs field" style="top:100px">Nasser</div>
      <div class="abs row-label" style="top:137px">Re-password</div>
      <div class="abs colon" style="top:137px">:</div>
      <div class="abs field" style="top:131px">knasser@mailbox.test</div>
      <div class="abs save">SAVE</div>
    </div>
  </div>

  <nav class="abs sub-nav">
    <a>CONTACT</a><i class="sep"></i><a>COPPERLEAF DEN</a><i class="sep"></i><a>CURRENCY CONVERTER</a>
  </nav>

  <div class="abs ornament" role="img" aria-label="Faint leafy vine pattern over the footer panel"></div>
  <div class="abs col-box" style="left:16px;width:211px"></div>
  <div class="abs col-box" style="left:235px;width:211px"></div>
  <div class="abs col-box" style="left:453px;width:212px"></div>
  <div class="abs col-box" style="left:675px;width:210px"></div>

  <div class="abs col-title" style="left:16px;width:211px">Popular Countries</div>
  <div class="abs col-title" style="left:235px;width:211px">Popular Cities</div>
  <div class="abs col-title" style="left:453px;width:212px">Top World Hotels</div>
  <div class="abs col-title" style="left:675px;width:210px">Login</div>

  <div class="abs country-list">Australia , Austria , England ,<br>France , Germany , Japan , Kenya ,<br>Malaysia , Maldives , Switzerland ,<br>Tanzania , Turkey , United Arab<br>, Emirates</div>
  <div class="abs city">, Athens</div>

  <div class="abs login-label" style="top:893px"><span>:</span>USERNAME</div>
  <div class="abs login-input" style="top:911px"></div>
  <div class="abs login-label" style="top:945px"><span>:</span>PASSWORD</div>
  <div class="abs login-input" style="top:963px"></div>
  <div class="abs login-link" style="top:1002px">?Forgot Password</div>
  <div class="abs login-link" style="top:1016px">Not Registered Yet? Signup<br>here</div>
  <div class="abs login-btn">LOGIN</div>

  <div class="abs footer-line"></div>
  <footer class="abs footer">
    <nav>TERMS OF SERVICE<span>|</span>ABOUT OUR ADS<span>|</span>PRIVACY POLICY<span>|</span>CONTACT<span>|</span>CURRENCY CONVERTER<span>|</span>MAPS<span>|</span>WEATHER<span>|</span>HOTELS<span>|</span>ABOUT<span>|</span>HOME</nav>
    <div class="copy">.Kefor Inc. All rights reserved 2012 ©</div>
  </footer>
</div>
</body>
</html>
```